| 希望する色 | 特になし・その他 追記事項: ブランドカラーについて添付URLに記載あり |
【 依頼内容 】 介護×美容を両方学べる社会人向けプロスクール「ひだまり整容学舎」のSNS広告バナーデザインを募集します。 当校HP:https://tsubakiho.jp/ ・配信媒体:Facebook / Instagram広告(フィード・ストーリーズ)/LINE広告 ・画像サイズ:1080px × 1080px(ピクセル) ※採用した方は追加で、1080px × 1920pxサイズの作成も依頼する場合がございます。 ・基本フォントは「游ゴシック」でお願いします ※手書き風のメッセージなど、明朝体のほうがバランスが良いなど理由がある場合は可。 遷移先のLP・作成用の素材・過去の制作物については添付URLをご参照ください。 【 契約金額(税抜) 】 5000円/デザイン (追加でサイズ違いの依頼の場合は2000円/デザイン) 3~5デザイン採用予定です! ※契約金額(税込)からシステム利用料を差し引いた金額が、ワーカーさまの受取金額となります 【依頼の目的】 SNS広告のキャッチコピーでターゲットの興味をグッと惹きつけ、Webページに誘導してまずは当スクールの資料請求をしてもらうことです。 (※SNS広告のイメージは添付ファイルをご覧ください) ターゲットは主に2種類いらっしゃいます 優先度髙【昔美容師をしていたが、出産でブランクがある。ママさん美容師】 ・子育ても落ち着いてきたので、美容師に戻ろうと思っている(戻った)が、拘束時間が長くなかな昔みたいに働けない。家庭との両立が難しいと考えている。 ⇒訪問美容師は遅くても夕方までの勤務なので、今までの経験を活かして働くことが出来ることを知らないママさん美容師に向けた、家庭との両立と副業感覚で短時間で稼げる事に興味を持ってもらう。 優先度低【美容師としてサロンに勤めている30歳前後】 ・独立も視野にあるスタイリスト経験ある美容師。一般的な美容院を作って独立することを視野にあるが、開業資金も高く美容室が増えているので不安がある。 ⇒お店を構えなくても良い「訪問美容師」なら、すぐに独立でき、高齢者が増えているのでこの先安泰では?と思えるようなコピー。 【依頼の背景】 ・訪問美容師とは? 主に介護施設や外出が困難な方向けに、こちらから訪問してカット・カラーなどの美容施術を行います。 ・訪問美容師の昔と今の違い 昔から、どの施設にもボランティアや理美容師さんが訪問をしてカットをしているが、昨今美容が好きな高齢者が増えている背景もあり、ただ髪を短くするだけじゃなく、美容室に行ったときのような施術を求められます。 ※ボランティアではなかなか実現しにくくなっている また、現在の訪問美容師さんは介護の知識を持っており、高齢者の応対もできるので、施設やご家族からは安心してもらえるのが、最近のスタンダードになっています。 ・訪問美容師のお仕事状況(弊社から依頼している案件ベース) 平日夕方までの実働:基本的には介護施設でご利用者さんの活動時間に訪問をする為 値段:地域性はあるが、カットお一人3000円~4500円ほどと一般的なサロンと変わらない値段 魅力:施設に伺う場合、お客様を選ぶというよりは毎週決まった時間に訪問して、施術を行うので、タイムスケジュールが決めやすいので、サロン勤務や家庭との両立も可能 ・ひだまり整容学舎で何を学ぶの? 訪問美容師デビューに向けた、テクニック、ビジネス、介護の初任者研修(資格取得)の講座を受けれる社会人向けスクール ※こちら参考にしてください※ 東京のビジネス講座の講師は、当校の1期生です。 参考Facebookページ:https://www.nakamaweb-sns.jp/tsubakiho.jp/posts/530287164912358 【重視するポイント】 ・「もっと知りたい!」「やってみたい!」とターゲットの興味を喚起し、クリックしてもらうことが目的です。 ・SNS広告で使用するので、表示された時に1秒で伝わるわかりやすさとインパクトは必須だと考えています。 ・文字数に具体的な制限はありませんが、トンマナも含め添付ファイルの既存広告をご参照ください。 【重要事項】 ①当校の広告は、スクールであることを重視しております。 業界的にも、画像的にも、よくご高齢者様に対してのサービスだと思われがちです。 そのサービスを提供する人材育成のスクールであることを念頭に入れて頂けると幸いです。 ②よりクリックしたく思わせるような「ティザー」の要素を加えて頂きたいです。 ※よく使うティザー例(違うフレーズでもOKです) 「今、訪問美容師が求められている3つの理由」 「家庭との両立が取りやすい理由とは?」 「ひだまり整容学舎が選ばれる理由とは?」 【年末年始について】 12/25~1/4まで冬期休暇をいただいております。 お問い合わせの回答にお時間を頂戴する場合がございますので、ご了承くださいませ。 その他ご質問等ありましたら、気軽にお問い合わせください。 ご応募をお待ちしております! |
| https://files.nerimo-docs.jp/document/d/8vQ2tRw5ZkLp0aXcYm3Hn7JsBd4FgEu9WiOy6TrKlMbN/edit | ||

```html
<!DOCTYPE html>
<html lang="ja">
<head>
<meta charset="UTF-8">
<title>訪問美容師 広告バナー</title>
<link href="https://fonts.googleapis.com/css2?family=Noto+Sans+JP:wght@500;700;900&display=swap" rel="stylesheet">
<style>
  :root{
    --pink:#e9336f;
    --pink-light:#f07aa0;
    --ink:#1c1c1c;
    --white:#ffffff;
    --photo-warm:#b98f6f;
    --photo-light:#e6d8cc;
    --photo-dark:#5a4538;
  }
  html,body{margin:0;padding:0;overflow:hidden;}
  body{width:1200px;height:1200px;background:var(--white);font-family:"Noto Sans JP",sans-serif;}
  .banner{position:relative;width:1200px;height:1200px;overflow:hidden;background:var(--white);}
  .hero-photo{
    position:absolute;left:0;top:0;width:1200px;height:1042px;
    background:
      radial-gradient(ellipse at 70% 30%, var(--photo-light) 0%, transparent 45%),
      radial-gradient(ellipse at 25% 85%, var(--photo-dark) 0%, transparent 50%),
      linear-gradient(135deg, #cdb5a3 0%, var(--photo-warm) 55%, #8a6a55 100%);
  }
  .headline{position:absolute;left:12px;top:128px;margin:0;}
  .headline span{display:block;width:max-content;font-weight:700;line-height:1;white-space:nowrap;}
  .line-1,.line-2{background:var(--white);color:var(--ink);font-size:80px;padding:26px 30px;letter-spacing:4px;}
  .line-1{margin-bottom:27px;}
  .line-2{margin-bottom:27px;}
  .line-3{background:var(--pink);color:var(--white);font-size:128px;font-weight:900;padding:21px 30px;letter-spacing:6px;}
  .teaser{
    position:absolute;right:0;top:0;width:155px;height:1042px;
    background:linear-gradient(180deg,var(--pink) 0%,var(--pink-light) 100%);
    display:flex;justify-content:center;align-items:flex-start;padding-top:36px;box-sizing:border-box;
  }
  .teaser p{
    margin:0;writing-mode:vertical-rl;color:var(--white);font-weight:700;font-size:52px;letter-spacing:3px;line-height:1;white-space:nowrap;
  }
  .footer{
    position:absolute;left:0;top:1042px;width:1200px;height:158px;
    display:flex;align-items:center;justify-content:space-between;padding:0 36px;box-sizing:border-box;background:var(--white);
  }
  .brand{display:flex;align-items:center;gap:14px;white-space:nowrap;}
  .brand-mark{width:30px;height:30px;background:var(--pink);flex:none;}
  .brand-name{font-size:36px;font-weight:500;color:var(--ink);letter-spacing:1px;white-space:nowrap;}
  .tagline{font-size:33px;font-weight:700;color:var(--ink);letter-spacing:1px;white-space:nowrap;}
</style>
</head>
<body>
<div class="banner">
  <div class="hero-photo" role="img" aria-label="美容師が高齢の方の髪をカットしている写真"></div>

  <h1 class="headline">
    <span class="line-1">キレイを</span>
    <span class="line-2">いつまでも届ける</span>
    <span class="line-3">訪問美容師</span>
  </h1>

  <div class="teaser"><p>ひだまり整容学舎が選ばれる理由とは？</p></div>

  <footer class="footer">
    <div class="brand">
      <span class="brand-mark"></span>
      <span class="brand-name">ひだまり整容学舎</span>
    </div>
    <div class="tagline">日本初！「介護×美容」の専門プロスクール</div>
  </footer>
</div>
</body>
</html>
```